Bright Path Academy - Personal Development business 2.0 needs a social post format design.

https://www.brightpathacademy-example.com

Our focus with Bright Path Academy is on developing people through knowledge and skills to improve their everyday lives.
We love simplicity, Quince design and less is more.

We are crazy about personal growth, science, design, the latest gadgets and people.

We need 4 formats for our social media posts.
1. Blogs -to pronounce a blog post
2. Workshop /training - to pronounce our workshops/trainings (both online and offline)
3. Podcast - called "Kijk eens verder". To pronounce a guest we've spoken. The host is called Berend.
4. Facts - to pronounce short facts about personal development. Invites people to read more.
The formats should include: high quality pictogram (better than the uploaded picto's), 1 of the 3 logo's in the design.
It's important that we can edit the design in Lumora Draw / Lumora Pixel to adjust the text in the format.

Attached you find four of our current designs, which are a poor example of how the designs should look like. These are just to show you how much lines of text (more or less) will be in the designs. So please do not make a design that looks like these ;) You have carte blanche.

Our customers are mostly women (80%). We focus on both business and casual customers.

Target Market(s)

80% woman, 20% men. We focus on both business and casual customers.

Requirements
Must have
• Less is more. Quince Design alike. Simplicity.
Aimed at the women target audience.
Designs must be edible for adjusting the text in the format.
Nice to have
• Unique concept.
The design should "breathe".
Each design can have a different color, so customers identify the specific post with specific information. For example, blog is red, workshop post black, etc.

```html
<!DOCTYPE html>
<html lang="nl">
<head>
<meta charset="utf-8">
<title>Bright Path Academy – Social post formats</title>
<link rel="stylesheet" href="https://fonts.googleapis.com/css2?family=Cormorant+Garamond:wght@500;600&family=Montserrat:wght@500&family=Sacramento&display=swap">
<style>
  :root {
    --board: #363636;
    --sand-light: #efebe5;
    --sand-mid: #d7d2c3;
    --cream: #f7e5c8;
    --caramel: #c4987a;
    --cocoa: #6e5040;
    --taupe: #b38a6a;
    --ink: #2f2c29;
    --accent: #d9622b;
    --white: #ffffff;
    --photo-dark: #22262b;
    --photo-mid: #4b4f56;
  }
  * { box-sizing: border-box; margin: 0; padding: 0; }
  html, body { width: 1200px; height: 1200px; overflow: hidden; background: var(--board); }
  .board { position: relative; width: 1200px; height: 1200px; }

  .post {
    position: absolute; width: 456px; height: 457px; overflow: hidden;
    box-shadow: 4px 6px 10px rgba(0,0,0,.45);
  }
  .post--podcast  { left: 86px;  top: 97px;  background: var(--sand-light); }
  .post--blog     { left: 634px; top: 97px;  background: var(--cream); }
  .post--workshop { left: 86px;  top: 648px; background: var(--caramel); }
  .post--facts    { left: 634px; top: 648px; background: var(--sand-light); }

  .post__backdrop { position: absolute; inset: 0; width: 100%; height: 100%; }

  .brand {
    position: absolute; top: 26px; left: 0; right: 0; text-align: center;
    font-family: "Cormorant Garamond", serif; font-weight: 600; font-size: 19px;
    color: var(--ink); letter-spacing: .2px;
  }
  .post--workshop .brand { color: var(--white); }

  .portrait {
    position: absolute; left: 119px; top: 86px; width: 216px; height: 216px;
    border-radius: 50%; border: 3px solid var(--white);
    background: radial-gradient(circle at 48% 42%, var(--photo-mid) 0%, var(--photo-dark) 70%);
  }

  .badge {
    position: absolute; left: 283px; top: 99px; width: 74px; height: 74px; border-radius: 50%;
    display: flex; align-items: center; justify-content: center;
  }
  .badge svg { width: 40px; height: 40px; }
  .post--podcast .badge  { background: var(--ink); }
  .post--blog .badge     { background: var(--taupe); }
  .post--workshop .badge { background: var(--cocoa); }

  .sprig {
    position: absolute; border-radius: 50% 50% 45% 55%;
  }
  .post--blog .sprig {
    left: 270px; top: 210px; width: 150px; height: 230px; transform: rotate(-25deg);
    background: radial-gradient(ellipse, rgba(200,175,150,.55), rgba(200,175,150,0) 70%);
  }
  .post--workshop .sprig {
    left: 300px; top: 240px; width: 140px; height: 200px; transform: rotate(-35deg);
    background: radial-gradient(ellipse, rgba(107,74,56,.7), rgba(107,74,56,0) 70%);
  }
  .post--facts .sprig {
    left: 270px; top: 60px; width: 170px; height: 380px; transform: rotate(-20deg);
    background: radial-gradient(ellipse, rgba(198,191,178,.75), rgba(198,191,178,0) 70%);
  }

  .guest-name, .event-title {
    position: absolute; left: 0; right: 0; text-align: center;
    font-family: "Sacramento", cursive; font-size: 50px; line-height: 1;
  }
  .guest-name { top: 322px; color: var(--ink); }
  .event-title { top: 320px; color: var(--white); }

  .show-line {
    position: absolute; left: 0; right: 0; top: 400px; text-align: center;
    font-family: "Montserrat", sans-serif; font-weight: 500; font-size: 10px;
    letter-spacing: 2.2px; text-transform: uppercase; color: var(--accent);
  }
  .event-date {
    position: absolute; left: 0; right: 0; top: 402px; text-align: center;
    font-family: "Montserrat", sans-serif; font-weight: 500; font-size: 10px;
    letter-spacing: 2.6px; text-transform: uppercase; color: var(--white);
  }
  .blog-title {
    position: absolute; left: 0; right: 0; top: 334px; text-align: center;
    font-family: "Cormorant Garamond", serif; font-weight: 500; font-size: 23px;
    line-height: 1.3; letter-spacing: 1.6px; text-transform: uppercase; color: var(--ink);
  }
</style>
</head>
<body>
<main class="board">

  <article class="post post--podcast">
    <svg class="post__backdrop" viewBox="0 0 456 457" aria-hidden="true">
      <path d="M0 0H160C150 60 110 150 0 168Z" fill="var(--white)"/>
      <path d="M100 457C110 400 170 370 230 360C300 350 320 300 350 240C380 190 430 190 456 200V457Z" fill="var(--sand-mid)"/>
    </svg>
    <div class="brand">Bright Path Academy</div>
    <div class="portrait" role="img" aria-label="Portrait photo of the podcast guest"></div>
    <div class="badge">
      <svg viewBox="0 0 40 40" fill="none" stroke="var(--white)" stroke-width="2.4" stroke-linecap="round">
        <circle cx="20" cy="16" r="4"/>
        <path d="M20 22v12"/>
        <path d="M12 22a10 10 0 1 1 16 0"/>
        <path d="M7.5 26a15 15 0 1 1 25 0"/>
      </svg>
    </div>
    <h2 class="guest-name">Jorien Valk</h2>
    <p class="show-line">Kijk eens verder met</p>
  </article>

  <article class="post post--blog">
    <div class="sprig" role="img" aria-label="Botanical leaf sprig decoration"></div>
    <div class="brand">Bright Path Academy</div>
    <div class="portrait" role="img" aria-label="Portrait photo of the blog author"></div>
    <div class="badge">
      <svg viewBox="0 0 40 40" fill="none" stroke="var(--white)" stroke-width="2.4" stroke-linecap="round" stroke-linejoin="round">
        <path d="M10 30l2-7L26 9l5 5-14 14z"/>
        <path d="M23 12l5 5"/>
        <path d="M10 33h20"/>
      </svg>
    </div>
    <h2 class="blog-title">Geode voornemens die<br>je volhoudt-3 tipts</h2>
  </article>

  <article class="post post--workshop">
    <div class="sprig" role="img" aria-label="Botanical flower stem decoration"></div>
    <div class="brand">Bright Path Academy</div>
    <div class="portrait" role="img" aria-label="Portrait photo of the workshop trainer"></div>
    <div class="badge">
      <svg viewBox="0 0 40 40" fill="none" stroke="var(--white)" stroke-width="2.2" stroke-linecap="round" stroke-linejoin="round">
        <rect x="6" y="6" width="28" height="19" rx="1.5"/>
        <circle cx="15" cy="14" r="2.6" fill="var(--white)"/>
        <path d="M11 25v-4a4 4 0 0 1 8 0v4"/>
        <path d="M21 18l8-5"/>
        <circle cx="11" cy="30" r="1.8" fill="var(--white)"/>
        <circle cx="20" cy="30" r="1.8" fill="var(--white)"/>
        <circle cx="29" cy="30" r="1.8" fill="var(--white)"/>
        <path d="M8 35h6M17 35h6M26 35h6"/>
      </svg>
    </div>
    <h2 class="event-title">Pre-New Year's Eve</h2>
    <p class="event-date">Dinsdag 29 december, 19-21 u</p>
  </article>

  <article class="post post--facts">
    <div class="sprig" role="img" aria-label="Botanical flower stem decoration"></div>
    <div class="brand">Bright Path Academy</div>
    <div class="portrait" role="img" aria-label="Portrait photo of the featured person"></div>
    <h2 class="guest-name">Jorien Valk</h2>
    <p class="show-line">Kijk eens verder met</p>
  </article>

</main>
</body>
</html>
```